Modern, cutting edge crypto trading website.

I need a single-page website design, approximate 4-5 pages. I have included a screenshot of the inside of the current application for some reference for what it currently looks like. This is the public side of the application for not logged in users.

I am currently thinking about 3-5 sections of the page.
Menu at top is optional, these could be the sections of the site.
1. Above the fold cool, grabbing stuff.
2. What problem does this solve
3. Additional benefits
4. Pricing
5. Open to ideas! Well it's all open to ideas if you have ideas.

I am nervous about hiring designers, I am open to a further discussion for more work for additional money but I have to LIKE your design. So this could be considered a trial. I would like to continue to design the application itself and match everything together!

I really like the tradewisp website.

Competitor websites:
https://7ridges.example/
https://www.tradewisp.example/

Target Market(s)

Adults 25-50 mostly male,

Number of Pages Required

4 page

Colors

Designer to choose colors to be used in the design.

Requirements
Must have
• Modern design, clean lines, professional.
Nice to have
• Fun SVG stuff. Not for this price, but in the future.
Should not have
• Should not be cluttered OR too spacey. Quince's website has too much open space sometimes.

```html
<!DOCTYPE html>
<html lang="en">
<head>
<meta charset="utf-8">
<title>Tradecue — The Chain for Trading Cryptocurrency</title>
<link href="https://fonts.googleapis.com/css2?family=Ubuntu:wght@500;700&family=Raleway:wght@300;400;500;600;700&display=swap" rel="stylesheet">
<style>
:root{
  --navy:#0d2458;
  --blue:#1c3fa8;
  --blue-mid:#3559c7;
  --blue-light:#6b8df0;
  --purple:#4a1a8c;
  --orange:#f26a0f;
  --red:#e8262b;
  --green:#2bb52b;
  --ink:#222;
  --text:#444;
  --grey-bg:#f5f5f7;
  --line:#c9c9d2;
  --pale:#e6ecfa;
  --heading:"Ubuntu",sans-serif;
  --body:"Raleway",sans-serif;
}
*{box-sizing:border-box;margin:0;padding:0}
html,body{width:1200px;height:4095px;overflow:hidden}
body{position:relative;background:#fff;font-family:var(--body);color:var(--text)}
.abs{position:absolute}
h1,h2,h3{font-family:var(--heading);font-weight:700}
.btn{position:absolute;display:flex;align-items:center;justify-content:center;font-family:var(--body);font-weight:700;font-size:13px;letter-spacing:.3px;text-transform:uppercase;border-radius:4px;color:#fff;background:var(--navy);text-decoration:none}
.btn-ghost{background:transparent;border:2px solid #fff}
p{font-size:14.5px;line-height:1.4}

/* nav */
.hero-blob{left:421px;top:0;width:779px;height:500px}
.logo{left:119px;top:58px;display:flex;align-items:center;gap:10px;font-family:var(--heading);font-weight:700;font-size:26px;color:var(--blue);letter-spacing:.5px}
.logo .mark{width:18px;height:18px;background:var(--blue);border-radius:3px}
.nav{left:579px;top:34px;display:flex;align-items:center;gap:38px}
.nav a{color:#fff;font-size:13.5px;font-weight:600;text-decoration:none}
.nav .login{border:2px solid #fff;border-radius:5px;padding:7px 14px}
.nav .signup{background:var(--red);border-radius:5px;padding:9px 14px;margin-left:-12px}

.hero-title{left:119px;top:142px;font-size:35px;line-height:46px;color:var(--blue)}
.hero-text{left:119px;top:289px;width:390px;font-size:14px;line-height:18px;color:#333}
.hero-art{left:525px;top:120px;width:560px;height:360px;border-radius:40%;background:radial-gradient(ellipse at center,#6f8cf5 0%,#3b5ad0 55%,rgba(59,90,208,0) 75%)}

/* partners */
.divider{left:119px;width:962px;height:0;border-top:1px dashed var(--line)}
.partners{left:210px;top:600px;width:790px;display:flex;justify-content:space-between;align-items:center}
.partners span{display:block;height:40px;border-radius:20px;background:#d5dcec}

/* services */
.center{left:0;width:1200px;text-align:center}
.sec-title{font-size:35px;line-height:46px;color:var(--ink)}
.sec-title em{font-style:normal;color:var(--blue)}
.pill{position:absolute;width:220px;height:66px;background:#fff;border-radius:16px;box-shadow:0 3px 10px rgba(0,0,0,.25);display:flex;align-items:center;gap:12px;padding:0 18px;font-family:var(--heading);font-weight:500;font-size:14px;line-height:17px;color:#222;text-align:center}
.pill svg{flex:none}
.pill span{flex:1}
.diamond{background:var(--orange);border-radius:26px;transform:rotate(45deg);box-shadow:0 6px 14px rgba(0,0,0,.2)}

/* pricing */
.pricing-bg{left:0;top:1189px;width:1200px;height:787px;background:var(--grey-bg)}
.features{left:119px;top:1394px;width:270px}
.features h3{font-family:var(--heading);font-weight:500;font-size:22px;color:#222;padding-bottom:12px;border-bottom:2px solid #555}
.features li{list-style:none;height:45px;display:flex;align-items:flex-end;padding-bottom:10px;border-bottom:1.5px solid #555;font-size:15px;color:#444}
.features li.price{font-weight:700;color:#222}
.plan{position:absolute;top:1375px;width:187px;height:551px;background:#fff;border-radius:14px;box-shadow:0 2px 10px rgba(0,0,0,.3);text-align:center}
.plan h3{font-family:var(--heading);font-weight:500;font-size:19px;color:#222;margin:22px 18px 0;padding-bottom:12px;border-bottom:1px solid var(--orange)}
.plan ul{margin:0 18px}
.plan li{list-style:none;height:45px;display:flex;align-items:center;justify-content:center;border-bottom:1px solid #eee}
.plan .amount{font-family:var(--heading);font-weight:500;font-size:21px;color:var(--blue);border:none}
.plan .btn{left:32px;bottom:20px;width:124px;height:46px;font-size:13px}

/* cta */
.cta{left:180px;top:2027px;width:840px;height:206px}
.cta-text{left:250px;top:2072px;width:430px;text-align:center;color:#fff;font-size:33px;line-height:48px}

/* bot */
.app-shot{left:153px;top:2348px;width:460px;height:264px;border-radius:6px;background:linear-gradient(90deg,#111 0 11%,#f1f2f5 11%)}
.app-blob{border-radius:50%;background:var(--blue-mid)}
.bot-title{left:688px;top:2276px;font-size:35px;line-height:46px;color:#222}
.bot-title em{font-style:normal;color:var(--blue)}
.bot-text{left:688px;width:390px;font-size:14px;line-height:20px;color:#444}

/* together */
.together-title{left:119px;top:2726px;font-size:35px;color:#222}
.together-text{left:119px;width:580px;font-size:15px;line-height:20px;color:#444}

/* clients */
.avatar{left:524px;top:3330px;width:150px;height:150px;border-radius:50%;border:3px solid #333;background:linear-gradient(160deg,#9aa3ad,#4a4f58)}
.dots{left:574px;top:3686px;display:flex;gap:5px}
.dots i{width:9px;height:9px;border-radius:50%;background:var(--blue-mid)}
.dots i:first-child{background:#555}

/* footer */
.foot-col{top:3796px}
.foot-col h4{font-family:var(--body);font-weight:600;font-size:13px;color:#222;margin-bottom:22px}
.foot-col p{font-size:11px;line-height:19px;color:#444}
.foot-col li{list-style:none;font-size:12px;color:#444;height:33px;display:flex;align-items:center;gap:10px}
.copy{left:0;top:4055px;width:1200px;text-align:center;font-size:11px;color:#333}
</style>
</head>
<body>
<svg width="0" height="0" style="position:absolute">
  <defs>
    <symbol id="tick" viewBox="0 0 24 24"><path d="M3 12.5l6 6L21 6" fill="none" stroke="#2bb52b" stroke-width="3.2" stroke-linecap="round" stroke-linejoin="round"/></symbol>
    <symbol id="cross" viewBox="0 0 24 24"><path d="M5 5l14 14M19 5L5 19" fill="none" stroke="#e8262b" stroke-width="3.2" stroke-linecap="round"/></symbol>
    <linearGradient id="heroGrad" x1="0" y1="0" x2="1" y2="1"><stop offset="0" stop-color="#2a47b8"/><stop offset=".6" stop-color="#4769d8"/><stop offset="1" stop-color="#9fb4f3"/></linearGradient>
    <linearGradient id="ctaGrad" x1="0" y1="0" x2="1" y2="0"><stop offset="0" stop-color="#6f8ff2"/><stop offset=".55" stop-color="#1c3a9e"/><stop offset="1" stop-color="#2d0f55"/></linearGradient>
    <linearGradient id="waveGrad" x1="0" y1="0" x2="1" y2="0"><stop offset="0" stop-color="#4c168e"/><stop offset=".5" stop-color="#1e3aa2"/><stop offset="1" stop-color="#3058d3"/></linearGradient>
    <linearGradient id="footGrad" x1="0" y1="0" x2="1" y2="1"><stop offset="0" stop-color="#5b7ce8"/><stop offset="1" stop-color="#1c3a9e"/></linearGradient>
  </defs>
</svg>

<!-- side decorations -->
<div class="abs" style="left:-30px;top:270px;width:60px;height:110px;border-radius:50%;background:var(--pale)"></div>
<div class="abs" style="left:-60px;top:840px;width:140px;height:330px;border-radius:45%;background:linear-gradient(180deg,#c8d4f3,#e9eefb)"></div>
<div class="abs" style="left:1050px;top:2110px;width:220px;height:170px;border-radius:50%;background:var(--pale)"></div>
<div class="abs" style="left:-70px;top:3420px;width:200px;height:210px;border-radius:50%;background:var(--pale)"></div>
<div class="abs" style="left:1120px;top:3420px;width:160px;height:220px;border-radius:50%;background:var(--pale)"></div>

<!-- hero -->
<header>
  <svg class="abs hero-blob" viewBox="0 0 779 500" aria-hidden="true">
    <path d="M0 0H779V330C700 400 600 480 480 470C360 460 300 380 230 300C150 210 60 150 20 60Z" fill="url(#heroGrad)"/>
  </svg>
  <div class="abs logo"><span class="mark"></span>Tradecue</div>
  <nav class="abs nav">
    <a href="#problems">Problems Solution</a>
    <a href="#pricing">Pricing</a>
    <a href="#benefits">Benifits</a>
    <a href="#login" class="login">LOG IN</a>
    <a href="#signup" class="signup">SIGN UP</a>
  </nav>
</header>

<section class="hero">
  <h1 class="abs hero-title">The Chain For<br>Trading<br>Cryptocurrency</h1>
  <p class="abs hero-text">Lorem ipsum dolor sit amet, consectetur adipiscing elit, sed do eiusmod tempor incididunt ut labore et dolore magna aliqua. Ut enim ad minim veniam, quis nostrud exercitation ullamco laboris nisi ut aliquip ex ea commodo consequat</p>
  <a class="btn" href="#start" style="left:119px;top:402px;width:123px;height:46px">Get Started</a>
  <div class="abs hero-art" role="img" aria-label="Isometric illustration of trading dashboards, coins and servers"></div>
</section>

<section class="partner-strip">
  <div class="abs divider" style="top:553px"></div>
  <div class="abs partners" aria-label="Partner badges">
    <span style="width:95px"></span><span style="width:130px"></span><span style="width:70px"></span><span style="width:110px"></span><span style="width:130px"></span>
  </div>
  <div class="abs divider" style="top:706px"></div>
</section>

<!-- services -->
<section id="problems">
  <h2 class="abs center sec-title" style="top:749px">Excellence is at the core of<br><em>our Service</em></h2>
  <p class="abs center" style="top:851px;font-size:14.5px;color:#444">It is our mission to provide the most trusted and comprehensive solution</p>

  <div class="pill" style="left:234px;top:917px"><svg width="34" height="34" viewBox="0 0 34 34"><path d="M17 3l12 7v14l-12 7-12-7V10z" fill="none" stroke="#222" stroke-width="2"/><circle cx="17" cy="17" r="5" fill="none" stroke="#222" stroke-width="2"/></svg><span>Crypto-Currency Application</span></div>
  <div class="pill" style="left:210px;top:995px"><svg width="36" height="34" viewBox="0 0 36 34"><rect x="2" y="3" width="32" height="28" rx="2" fill="none" stroke="#222" stroke-width="2"/><path d="M2 10h32M8 16h8v9H8zM20 16h8v9h-8z" fill="none" stroke="#222" stroke-width="2"/></svg><span>UI/UX for Mobile Application</span></div>
  <div class="pill" style="left:234px;top:1074px"><svg width="38" height="30" viewBox="0 0 38 30"><rect x="13" y="10" width="12" height="10" fill="none" stroke="#222" stroke-width="2"/><path d="M19 1v7M10 3l4 5M28 3l-4 5M2 15h9M27 15h9M15 25h8" fill="none" stroke="#222" stroke-width="2"/></svg><span>IT Infrastruction Management</span></div>

  <div class="abs diamond" style="left:528px;top:954px;width:146px;height:146px" role="img" aria-label="Orange brand emblem"></div>

  <div class="pill" style="left:747px;top:917px"><svg width="22" height="36" viewBox="0 0 22 36"><circle cx="11" cy="10" r="7" fill="none" stroke="#222" stroke-width="2"/><circle cx="11" cy="27" r="7" fill="none" stroke="#222" stroke-width="2"/></svg><span>iOS Application Development</span></div>
  <div class="pill" style="left:769px;top:995px"><svg width="40" height="34" viewBox="0 0 40 34"><path d="M4 4h22v14H12l-6 5v-5H4z M16 18v6h14l6 5v-5h2V10h-8" fill="none" stroke="#222" stroke-width="2" stroke-linejoin="round"/></svg><span>Bot Chat Application</span></div>
  <div class="pill" style="left:747px;top:1074px"><svg width="34" height="38" viewBox="0 0 34 38"><path d="M7 16a10 10 0 0 1 20 0z M7 18h20v13H7z M3 18v10M31 18v10M12 31v5M22 31v5M11 7l-3-4M23 7l3-4" fill="none" stroke="#222" stroke-width="2"/></svg><span>Android Application Development</span></div>
</section>

<!-- pricing -->
<section id="pricing">
  <div class="abs pricing-bg"></div>
  <h2 class="abs center sec-title" style="top:1232px;font-size:33px">Pricing</h2>
  <p class="abs" style="left:130px;top:1288px;width:940px;text-align:center;font-size:14.5px;line-height:20px">Lorem ipsum dolor sit amet, consectetur adipiscing elit. Praesent bibendum odio id semper malesuada. Duis scelerisque lorem eu nibh dignissim posuere. Nam non commodo eros, et consectetur velit. In gravida, diam vel egestas tincidunt.</p>

  <div class="abs features">
    <h3>Features Included</h3>
    <ul>
      <li>Trading terminal</li>
      <li>Concurrent Take Profit and Stop Loss</li>
      <li>ChartView Custom Signals</li>
      <li>Simple bots</li>
      <li>Short and Long algorithms</li>
      <li>View and copy bots</li>
      <li>Composite bots</li>
      <li>Kraxa and Bylo bots</li>
      <li class="price">Price</li>
    </ul>
  </div>

  <article class="plan" style="left:466px">
    <h3>Starter Package</h3>
    <ul>
      <li><svg width="24" height="24"><use href="#tick"/></svg></li>
      <li><svg width="24" height="24"><use href="#tick"/></svg></li>
      <li><svg width="20" height="20"><use href="#cross"/></svg></li>
      <li><svg width="20" height="20"><use href="#cross"/></svg></li>
      <li><svg width="20" height="20"><use href="#cross"/></svg></li>
      <li><svg width="20" height="20"><use href="#cross"/></svg></li>
      <li><svg width="20" height="20"><use href="#cross"/></svg></li>
      <li><svg width="20" height="20"><use href="#cross"/></svg></li>
      <li class="amount">$60</li>
    </ul>
    <a class="btn" href="#starter">Get Started</a>
  </article>
  <article class="plan" style="left:680px">
    <h3>Basic Startup</h3>
    <ul>
      <li><svg width="24" height="24"><use href="#tick"/></svg></li>
      <li><svg width="24" height="24"><use href="#tick"/></svg></li>
      <li><svg width="24" height="24"><use href="#tick"/></svg></li>
      <li><svg width="24" height="24"><use href="#tick"/></svg></li>
      <li><svg width="24" height="24"><use href="#tick"/></svg></li>
      <li><svg width="24" height="24"><use href="#tick"/></svg></li>
      <li><svg width="20" height="20"><use href="#cross"/></svg></li>
      <li><svg width="20" height="20"><use href="#cross"/></svg></li>
      <li class="amount">$99</li>
    </ul>
    <a class="btn" href="#basic">Get Started</a>
  </article>
  <article class="plan" style="left:893px">
    <h3>Professional</h3>
    <ul>
      <li><svg width="24" height="24"><use href="#tick"/></svg></li>
      <li><svg width="24" height="24"><use href="#tick"/></svg></li>
      <li><svg width="24" height="24"><use href="#tick"/></svg></li>
      <li><svg width="24" height="24"><use href="#tick"/></svg></li>
      <li><svg width="24" height="24"><use href="#tick"/></svg></li>
      <li><svg width="24" height="24"><use href="#tick"/></svg></li>
      <li><svg width="24" height="24"><use href="#tick"/></svg></li>
      <li><svg width="24" height="24"><use href="#tick"/></svg></li>
      <li class="amount">$199</li>
    </ul>
    <a class="btn" href="#pro">Get Started</a>
  </article>
</section>

<!-- call to action -->
<section class="cta-block">
  <svg class="abs cta" viewBox="0 0 840 206" aria-hidden="true">
    <path d="M8 210L838 185V0H40Z" fill="rgba(0,0,0,.55)" transform="translate(0,-4)"/>
    <path d="M0 200L835 175V0H40Z" fill="url(#ctaGrad)"/>
  </svg>
  <h2 class="abs cta-text">Ready to get started<br>Join us right now!</h2>
  <svg class="abs" style="left:600px;top:2105px" width="160" height="60" viewBox="0 0 160 60" aria-hidden="true"><path d="M5 45C60 60 105 50 150 10M135 8l15 2-4 14" fill="none" stroke="#9fb4f3" stroke-width="2.5" stroke-linecap="round"/></svg>
  <a class="btn btn-ghost" href="#join" style="left:728px;top:2084px;width:178px;height:47px;background:transparent">Join Now</a>
</section>

<!-- bot -->
<section id="benefits">
  <div class="abs app-blob" style="left:120px;top:2380px;width:90px;height:110px;background:var(--blue)"></div>
  <div class="abs app-blob" style="left:280px;top:2292px;width:140px;height:120px"></div>
  <div class="abs app-blob" style="left:445px;top:2600px;width:36px;height:30px;background:var(--purple)"></div>
  <div class="abs app-shot" role="img" aria-label="Screenshot of the trading bot strategies dashboard" style="box-shadow:0 3px 12px rgba(0,0,0,.15)"></div>

  <h2 class="abs bot-title">Your Personal<br><em>Crypto Trading Bot</em></h2>
  <p class="abs bot-text" style="top:2381px">Lorem ipsum dolor sit amet, consectetur adipiscing elit. Praesent bibendum odio id semper malesuada. Duis scelerisque lorem eu nibh dignissim posuere. Nam non commodo eros, et consectetur velit. In gravida, diam vel egestas tincidunt.</p>
  <p class="abs bot-text" style="top:2500px">Praesent bibendum odio id semper malesuada. Duis scelerisque lorem eu nibh dignissim posuere. Nam non commodo eros, et consectetur velit. In gravida, diam vel egestas tincidunt.</p>
  <a class="btn" href="#signup" style="left:687px;top:2602px;width:108px;height:43px">Sign Up</a>
</section>

<!-- together -->
<section class="together">
  <svg class="abs" style="left:0;top:2780px" width="1200" height="460" viewBox="0 0 1200 460" aria-hidden="true">
    <path d="M0 170C200 195 400 225 620 200C820 175 1000 100 1200 0V406C1000 370 850 330 650 335C450 340 250 380 0 455Z" fill="url(#waveGrad)"/>
  </svg>
  <h2 class="abs together-title">Together. We make Innovative Things</h2>
  <p class="abs together-text" style="top:2785px">Lorem ipsum dolor sit amet, consectetur adipiscing elit. Praesent bibendum odio id semper malesuada. Duis scelerisque lorem eu nibh dignissim posuere. Nam non commodo eros, et consectetur velit. In gravida, diam vel egestas tincidunt.</p>
  <p class="abs together-text" style="top:2876px">Praesent bibendum odio id semper malesuada. Duis scelerisque lorem eu nibh dignissim posuere. Nam non commodo eros, et consectetur velit. In gravida, diam vel egestas tincidunt.</p>
  <a class="btn btn-ghost" href="#contact" style="left:262px;top:3034px;width:178px;height:50px">Contact Us Today</a>
  <div class="abs diamond" style="left:823px;top:2888px;width:214px;height:214px;border-radius:36px" role="img" aria-label="Orange brand emblem"></div>
</section>

<!-- clients -->
<section class="clients">
  <h2 class="abs center sec-title" style="top:3218px;font-size:34px">Our Clients Love Us</h2>
  <p class="abs center" style="top:3276px;font-size:15px">They are simply great</p>
  <div class="abs avatar" role="img" aria-label="Portrait photo of client Marcus Hale"></div>
  <p class="abs center" style="top:3505px;font-size:16px;font-weight:700;color:#222">Marcus Hale</p>
  <p class="abs" style="left:190px;top:3547px;width:820px;text-align:center;font-size:15px;line-height:20px">Lorem ipsum dolor sit amet, consectetur adipiscing elit. Praesent bibendum odio id semper malesuada. Duis scelerisque lorem eu nibh dignissim posuere. Nam non commodo eros, et consectetur velit. In gravida, diam vel egestas tincidunt.</p>
  <p class="abs" style="left:190px;top:3626px;width:820px;text-align:center;font-size:15px;line-height:20px">Praesent bibendum odio id semper malesuada. Duis scelerisque lorem eu nibh dignissim posuere. Nam non commodo eros, et consectetur velit. In gravida, diam vel egestas tincidunt.</p>
  <div class="abs dots"><i></i><i></i><i></i><i></i></div>
</section>

<!-- footer -->
<footer id="contact">
  <svg class="abs" style="left:921px;top:3900px" width="279" height="195" viewBox="0 0 279 195" aria-hidden="true"><path d="M0 195C40 120 120 40 279 0V195Z" fill="url(#footGrad)"/></svg>
  <div class="abs divider" style="top:3748px;border-top:1.5px solid #c9d2ea"></div>
  <div class="abs foot-col" style="left:119px;width:310px">
    <h4>More About Company</h4>
    <p>Lorem ipsum dolor sit amet, consectetur adipiscing elit. Duis dapibus rhoncus purus, quis aliquet urna vehicula eu. Maecenas velit orci, volutpat sed posuere eu, vehicula eu tellus. Pellentesque sem sapien, aliquet id rhoncus eget, interdum vitae ligula.</p>
    <p style="text-align:right;margin-top:16px;padding-right:20px">- Daniel Orrin, CEO</p>
  </div>
  <div class="abs foot-col" style="left:464px">
    <h4>QUICK LINKS</h4>
    <ul style="padding-left:22px;margin-top:-6px">
      <li>Problems Solution</li><li>Pricing</li><li>Testimonials</li><li>Contact Us</li>
    </ul>
  </div>
  <div class="abs foot-col" style="left:798px">
    <h4>Contact Information</h4>
    <ul style="margin-top:-6px">
      <li><svg width="16" height="14" viewBox="0 0 16 14"><path d="M8 0L0 7h2v7h4V9h4v5h4V7h2z" fill="#222"/></svg>Plant B. Manager</li>
      <li style="padding-left:26px">14 Larkspur Row</li>
      <li style="padding-left:26px">Eastmere, EM4 2QT</li>
      <li><svg width="16" height="16" viewBox="0 0 16 16"><rect x="4" y="1" width="8" height="14" rx="1.5" fill="none" stroke="#222" stroke-width="2"/></svg>0800 555 0199</li>
      <li><svg width="16" height="12" viewBox="0 0 16 12"><rect x="1" y="1" width="14" height="10" fill="none" stroke="#222" stroke-width="1.6"/><path d="M1 1l7 6 7-6" fill="none" stroke="#222" stroke-width="1.6"/></svg><span style="color:#2a55d0">contact@example.com</span></li>
    </ul>
  </div>
  <p class="abs copy">Copyright @ 2019Company Name. All rights reserved.</p>
</footer>
</body>
</html>
```